Business letterhead and powerpoint template

Hi, I have recently started using a new logo (found through MarkVesta) and would now like to use that logo for letterheads and powerpoint.

Attached is the logo and one version of a brochure I have recently used.

Business

```html
<!DOCTYPE html>
<html lang="en">
<head>
<meta charset="utf-8">
<title>Halden Capital – Slide Templates</title>
<link rel="stylesheet" href="https://fonts.googleapis.com/css2?family=Exo+2:wght@300;400&display=swap">
<style>
  :root {
    --stage-top: #3c3f40;
    --stage-bottom: #ecebe7;
    --slide-light: #ffffff;
    --slide-dark: #161819;
    --mark-light: #f3f3f3;
    --mark-dark: #1f2223;
    --accent: #ff3b14;
    --ink-dark: #2a2a2a;
    --ink-light: #f2f2f2;
    --rule-grey: #b8b8b8;
  }
  * { box-sizing: border-box; margin: 0; padding: 0; }
  html, body { width: 1200px; height: 656px; overflow: hidden; }
  body {
    position: relative;
    font-family: "Exo 2", sans-serif;
    background: linear-gradient(to bottom, var(--stage-top) 0 337px, var(--stage-bottom) 337px 100%);
  }
  .slide {
    position: absolute;
    width: 327px;
    height: 242px;
    overflow: hidden;
    box-shadow: 10px 12px 14px rgba(0,0,0,0.45);
  }
  .slide--light { background: var(--slide-light); }
  .slide--dark { background: var(--slide-dark); box-shadow: 10px 12px 14px rgba(0,0,0,0.35); }
  .row-top { top: 60px; }
  .row-bottom { top: 370px; }
  .col-1 { left: 56px; }
  .col-2 { left: 437px; }
  .col-3 { left: 815px; }

  .backdrop-mark {
    position: absolute;
    left: 24px;
    top: 62px;
    display: flex;
    align-items: center;
    gap: 14px;
    font-size: 64px;
    font-weight: 400;
    letter-spacing: 3px;
    line-height: 1;
    white-space: nowrap;
  }
  .backdrop-mark::before {
    content: "";
    width: 34px;
    height: 34px;
    background: currentColor;
  }
  .slide--light .backdrop-mark { color: var(--mark-light); }
  .slide--dark .backdrop-mark { color: var(--mark-dark); }

  .title-lockup {
    position: absolute;
    right: 40px;
    bottom: 32px;
    text-align: center;
  }
  .title-lockup .name {
    display: flex;
    align-items: center;
    gap: 8px;
    font-size: 30px;
    font-weight: 300;
    letter-spacing: 1px;
    line-height: 1;
  }
  .title-lockup .name::before,
  .footer-band .badge::before {
    content: "";
    background: var(--accent);
    flex: none;
  }
  .title-lockup .name::before { width: 16px; height: 16px; }
  .title-lockup .tagline {
    display: flex;
    align-items: center;
    gap: 6px;
    margin-top: 5px;
    font-size: 8px;
    font-weight: 300;
    letter-spacing: 2px;
    color: var(--rule-grey);
  }
  .title-lockup .tagline::before,
  .title-lockup .tagline::after {
    content: "";
    flex: 1;
    height: 1px;
    background: var(--rule-grey);
  }
  .slide--light .name { color: var(--ink-dark); }
  .slide--dark .name { color: var(--ink-light); }

  .footer-band {
    position: absolute;
    left: 0; right: 0; bottom: 0;
    height: 11px;
    display: flex;
    align-items: flex-end;
  }
  .footer-band .bar { flex: 1; height: 11px; background: var(--accent); }
  .footer-band .badge {
    width: 77px;
    height: 17px;
    display: flex;
    align-items: center;
    justify-content: center;
    gap: 4px;
    font-size: 9px;
    font-weight: 400;
    letter-spacing: 0.5px;
    line-height: 1;
  }
  .footer-band .badge::before { width: 6px; height: 6px; }
  .slide--light .badge { background: var(--slide-light); color: var(--ink-dark); }
  .slide--dark .badge { background: var(--slide-dark); color: var(--ink-light); }
</style>
</head>
<body>
  <section class="slide slide--light row-top col-1">
    <span class="backdrop-mark" aria-hidden="true">HALDEN</span>
    <div class="title-lockup">
      <span class="name">HALDEN</span>
      <span class="tagline">CAPITAL</span>
    </div>
  </section>
  <section class="slide slide--light row-top col-2">
    <span class="backdrop-mark" aria-hidden="true">HALDEN</span>
    <div class="footer-band"><span class="bar"></span><span class="badge">HALDEN</span></div>
  </section>
  <section class="slide slide--light row-top col-3">
    <span class="backdrop-mark" aria-hidden="true">HALDEN</span>
  </section>

  <section class="slide slide--dark row-bottom col-1">
    <span class="backdrop-mark" aria-hidden="true">HALDEN</span>
    <div class="title-lockup">
      <span class="name">HALDEN</span>
      <span class="tagline">CAPITAL</span>
    </div>
  </section>
  <section class="slide slide--dark row-bottom col-2">
    <span class="backdrop-mark" aria-hidden="true">HALDEN</span>
    <div class="footer-band"><span class="bar"></span><span class="badge">HALDEN</span></div>
  </section>
  <section class="slide slide--dark row-bottom col-3">
    <span class="backdrop-mark" aria-hidden="true">HALDEN</span>
  </section>
</body>
</html>
```